Lawn Sign Design

I'm looking for a new lawn sign design to help promote our landscape company. We're trying to position ourselves as a leader in our market, so obviously quality and elegance are important to us.

Phone Number: (555) 214-3098
Website: verdalquix.com
Our tagline: "Your hands are full... Let us help"

Full Service
Weekly Sawn Service
Lanscape Lighting
Spring/Fall Clean Ups
Turf Edging
Snow Removal

I have attached a jpg of our logo to help with design colors. I will provide the vector file upon completion of this project.

Feel free to use your imagination. I know little about content of effective lawn signs, so I'm relying a lot on you, the professionals.

Thanks
Updates

Project Deadline Extended
Reason: Haven't found what I'm looking for.

Industry/Entity Type

Landscape

Requirements
Must have
• Class, elegance, professionalism.
Should not have
• Tacky cartoonish looking desings

```html
<!DOCTYPE html>
<html lang="en">
<head>
<meta charset="utf-8">
<title>Verdalquix Landscaping Lawn Sign</title>
<link href="https://fonts.googleapis.com/css2?family=Cinzel:wght@700&family=Noto+Serif:wght@700&family=Roboto+Slab:wght@400&display=swap" rel="stylesheet">
<style>
  :root {
    --backdrop: #344a36;
    --olive: #86a812;
    --forest: #006837;
    --white: #ffffff;
    --leaf-light: #c4dc5a;
    --leaf-mid: #8db22a;
    --leaf-dark: #3f7f22;
    --badge: #e8602a;
  }
  * { margin: 0; padding: 0; box-sizing: border-box; }
  html, body {
    width: 1200px; height: 1000px; overflow: hidden;
    background: var(--backdrop);
  }
  .sign {
    position: absolute; left: 236px; top: 156px;
    width: 723px; height: 542px;
    background: var(--white);
  }
  .brand-band {
    position: absolute; left: 0; top: 0; width: 100%; height: 100px;
    background: var(--olive);
    display: flex; align-items: center; justify-content: center; gap: 10px;
  }
  .brand-dot {
    width: 22px; height: 22px; border-radius: 50%;
    background: var(--badge);
  }
  .brand-name {
    font-family: "Noto Serif", Georgia, serif; font-weight: 700;
    font-size: 22px; letter-spacing: 2px; color: var(--white);
  }
  .headline {
    position: absolute; left: 0; top: 100px; width: 723px; height: 130px;
  }
  .headline text {
    font-family: "Cinzel", "Times New Roman", serif; font-weight: 700;
    fill: var(--forest);
  }
  .home-illustration {
    position: absolute; left: 144px; top: 180px; width: 432px; height: 172px;
    border-radius: 50% 50% 8px 8px / 60% 60% 8px 8px;
    background: linear-gradient(180deg, var(--leaf-mid) 0%, var(--leaf-light) 55%, var(--leaf-dark) 100%);
    opacity: .85;
  }
  .tagline-band {
    position: absolute; left: 0; top: 361px; width: 100%; height: 85px;
    background: var(--forest);
    display: flex; align-items: center; justify-content: center;
    font-family: "Noto Serif", Georgia, serif; font-weight: 700;
    font-size: 35px; color: var(--white);
  }
  .contact {
    position: absolute; left: 0; top: 446px; width: 100%; height: 96px;
    display: flex; align-items: center; justify-content: center; gap: 34px;
    font-family: "Roboto Slab", Georgia, serif; color: var(--forest);
  }
  .contact-phone { font-size: 54px; }
  .contact-web { font-size: 30px; }
</style>
</head>
<body>
  <div class="sign">
    <div class="brand-band">
      <span class="brand-dot"></span>
      <span class="brand-name">VERDALQUIX</span>
    </div>

    <svg class="headline" viewBox="0 0 723 130" aria-label="Landscaping">
      <defs>
        <path id="headline-arc" d="M 52 99 Q 362 20 671 99"/>
      </defs>
      <text font-size="70" textLength="612" lengthAdjust="spacingAndGlyphs">
        <textPath href="#headline-arc">L<tspan font-size="56">ANDSCAPING</tspan></textPath>
      </text>
    </svg>

    <div class="home-illustration" role="img" aria-label="Illustration of a house with trees on rolling green lawn"></div>

    <div class="tagline-band">"Your hands are full...Let us help."</div>

    <div class="contact">
      <span class="contact-phone">555.214.3098</span>
      <span class="contact-web">verdalquix.com</span>
    </div>
  </div>
</body>
</html>
```